Hacienda Valle Dorado Business cards

We would like 3 individual business cards with the logo you designed:

1) Marta Pellworth - Phone: 206 555 0147
2) Theodore K Pellworth - Phone 206 555 0183
3) Dana Whitlow - Phone 310-555-0126

Address for all three cards:
4217 288th Ave NE
Carnation, WA 98019
HaciendaValleDorado@mailbox-example.com

```html
<!DOCTYPE html>
<html lang="en">
<head>
<meta charset="utf-8">
<title>Hacienda Valle Dorado – Business Card</title>
<link rel="stylesheet" href="https://fonts.googleapis.com/css2?family=Cinzel:wght@500&family=Marcellus+SC&display=swap">
<style>
  :root {
    --frame: #000000;
    --paper: #ffffff;
    --ink: #111111;
    --mark-dark: #1a1a1a;
    --mark-light: #6a6a6a;
  }
  html, body {
    margin: 0;
    padding: 0;
    width: 1200px;
    height: 746px;
    overflow: hidden;
    background: var(--frame);
  }
  .canvas {
    position: relative;
    width: 1200px;
    height: 746px;
    background: var(--frame);
  }
  .card {
    position: absolute;
    left: 145px;
    top: 0;
    width: 910px;
    height: 746px;
    background: var(--paper);
    color: var(--ink);
  }
  .brand-emblem {
    position: absolute;
    left: 345px;
    top: 120px;
    width: 240px;
    height: 240px;
  }
  .brand-name {
    position: absolute;
    left: 0;
    top: 400px;
    width: 100%;
    margin: 0;
    text-align: center;
    font-family: "Cinzel", serif;
    font-weight: 500;
    font-size: 46px;
    letter-spacing: 1px;
    line-height: 1;
    color: var(--ink);
  }
  .contact {
    position: absolute;
    left: 0;
    top: 535px;
    width: 100%;
    text-align: center;
    font-family: "Marcellus SC", serif;
    font-size: 23px;
    letter-spacing: 1.5px;
    line-height: 28.5px;
    font-style: normal;
  }
  .contact p {
    margin: 0;
  }
  .contact .gap {
    margin-top: 28px;
  }
</style>
</head>
<body>
<main class="canvas">
  <section class="card">
    <svg class="brand-emblem" viewBox="0 0 240 240" role="img" aria-label="Ranch emblem: tree beside a fence with horses and birds">
      <defs>
        <radialGradient id="emblemShade" cx="40%" cy="35%" r="70%">
          <stop offset="0" stop-color="var(--mark-light)"/>
          <stop offset="1" stop-color="var(--mark-dark)"/>
        </radialGradient>
      </defs>
      <circle cx="120" cy="120" r="118" fill="url(#emblemShade)"/>
    </svg>

    <h1 class="brand-name">Hacienda Valle Dorado</h1>

    <address class="contact">
      <p class="person">Theodore K Pellworth</p>
      <p class="phone">206-555-0183</p>
      <p class="street gap">4217 288th Ave NE</p>
      <p class="city">Carnation, WA 98019</p>
      <p class="email">HaciendaValleDorado@mailbox-example.com</p>
    </address>
  </section>
</main>
</body>
</html>
```